Defense Attorney Business Card Design Project/ Stationary

I am looking for a distinctive business card design for my solo law practice.
I practice criminal defense, both juvenile and adult, including DUI. I am a very experienced attorney with prior military experience. The design should convey a traditional, old school flair, but not be too stodgy or uptight. Some color. My logo should appear.

Project Deadline Extended Reason: I misunderstood how this project works and I was not prepared with my logo when this project ran the first time. Added Thursday, November 13, 2014

Reason: I was sent overseas on military duty last year, which interrupted this project. Thank you for your participation... I hope we can get this done this week! Thank you, Des

Target Market(s)

Regular everyday people looking for strong, knowledgeable, authoritative representation while they are faced with criminal charges. Many have never been charged with a crime before. A reassuring air is therefore desired.

Industry/Entity Type

Business

Contact Information for Business Card

My information is:
Desmond R. Whitcombe, Attorney at Law
735 Linden Avenue Suite 300
Oakland, California 94618
Tel: (510) 555-0183
Fax: (510) 555-0162
email: deswhitcombelaw@mailbrook.net
web: www.deswhitcombelaw.net

Font styles to use
Serif
Sans Serif
Decorative

Colors
0255a3
ffffff

Requirements
Must have
• Sharp lines, bold elements. Conservative use of colors, such as deep blues, burgundy, grays for example.
• While my logo says "Des Whitcombe", it should be modified to show "Desmond R. Whitcombe".
Should not have
• Cliche imagery such as scales of justice, gavels, Tower of Varenholt, etc.

```html
<!DOCTYPE html>
<html lang="en">
<head>
<meta charset="utf-8">
<title>Desmond R. Whitcombe – Business Cards</title>
<link rel="stylesheet" href="https://fonts.googleapis.com/css2?family=Cinzel:wght@400;500&family=Montserrat:wght@300;400&display=swap">
<style>
  :root {
    --page: #f1f1f0;
    --card-dark: #2a2828;
    --card-navy: #1d3550;
    --cream: #d8cdac;
    --cream-soft: #cfc5a6;
  }
  * { box-sizing: border-box; margin: 0; padding: 0; }
  html, body {
    width: 1200px;
    height: 696px;
    overflow: hidden;
    background: var(--page);
  }
  .canvas {
    position: relative;
    width: 1200px;
    height: 696px;
  }
  .card {
    position: absolute;
    color: var(--cream);
  }

  /* Contact card (portrait) */
  .card--contact {
    left: 150px;
    top: 68px;
    width: 320px;
    height: 560px;
    background: var(--card-dark);
    padding: 44px 36px;
  }
  .brand-mark {
    display: flex;
    align-items: center;
    justify-content: center;
    gap: 8px;
    white-space: nowrap;
    font-family: "Cinzel", serif;
    font-weight: 500;
    font-size: 14px;
    letter-spacing: 0.03em;
    color: var(--cream);
  }
  .brand-mark__dot {
    width: 7px;
    height: 7px;
    border-radius: 50%;
    background: var(--cream);
    flex: none;
  }
  .divider {
    width: 22px;
    height: 2px;
    background: var(--cream);
    margin: 30px 0 20px;
  }
  .attorney-name {
    font-family: "Cinzel", serif;
    font-size: 14px;
    letter-spacing: 0.03em;
    line-height: 1.5;
  }
  .attorney-role,
  .contact-list {
    font-family: "Montserrat", sans-serif;
    font-weight: 300;
    font-size: 11.5px;
    line-height: 1.6;
    color: var(--cream-soft);
  }
  .contact-list { list-style: none; }
  .address {
    font-family: "Cinzel", serif;
    font-style: normal;
    font-size: 12.5px;
    line-height: 1.6;
    letter-spacing: 0.02em;
  }

  /* Brand card (landscape) */
  .card--brand {
    left: 570px;
    top: 300px;
    width: 560px;
    height: 320px;
    background: var(--card-navy);
  }
  .brand-lockup {
    position: absolute;
    left: 0;
    right: 0;
    top: 122px;
    display: flex;
    align-items: center;
    justify-content: center;
    gap: 12px;
    white-space: nowrap;
    font-family: "Cinzel", serif;
    font-weight: 500;
    font-size: 29px;
    letter-spacing: 0.02em;
    color: var(--cream);
  }
  .brand-lockup__dot {
    width: 11px;
    height: 11px;
    border-radius: 50%;
    background: var(--cream);
    flex: none;
  }
  .card--brand .divider {
    position: absolute;
    left: 176px;
    top: 206px;
    margin: 0;
  }
  .website {
    position: absolute;
    left: 176px;
    top: 222px;
    font-family: "Montserrat", sans-serif;
    font-weight: 300;
    font-size: 14px;
    color: var(--cream-soft);
  }
</style>
</head>
<body>
<main class="canvas">

  <section class="card card--contact">
    <div class="brand-mark">
      <span class="brand-mark__dot"></span>
      <span>Desmond R. Whitcombe</span>
    </div>

    <div class="divider"></div>
    <p class="attorney-name">DESMOND R. WHITCOMBE</p>
    <p class="attorney-role">Attorney at Law (Criminal Defense)</p>

    <div class="divider"></div>
    <ul class="contact-list">
      <li>T: (510) 555-0183</li>
      <li>F: (510) 555-0162</li>
      <li>E: deswhitcombelaw@mailbrook.net</li>
      <li>W: www.deswhitcombelaw.net</li>
    </ul>

    <div class="divider"></div>
    <address class="address">
      735 Linden Avenue, Suite 300<br>
      Oakland, California 94618
    </address>
  </section>

  <section class="card card--brand">
    <div class="brand-lockup">
      <span class="brand-lockup__dot"></span>
      <span>Desmond R. Whitcombe</span>
    </div>
    <div class="divider"></div>
    <p class="website">deswhitcombelaw.net</p>
  </section>

</main>
</body>
</html>
```